Calm Harbor Blueprint

I need a on page electronic flyer for this coaching program. I want a silhouette to accompany the case the copy starts with. I have the copy written but need it put together in a striking way.

Target Market(s)

towards higher net worth individuals

Industry/Entity Type

Electronic

```html
<!DOCTYPE html>
<html lang="en">
<head>
<meta charset="utf-8">
<title>Calm Harbor Blueprint – Coaching Flyer</title>
<link rel="stylesheet" href="https://fonts.googleapis.com/css2?family=Roboto+Slab:wght@700;800;900&family=Arimo:wght@400;700&display=swap">
<style>
:root{
  --cream:#fbf3b8;
  --paper:#ffffff;
  --ink:#000000;
  --red:#e0141b;
  --violet:#3a2a8f;
  --yellow:#ffe61a;
  --lime:#b8e34a;
  --green:#7ed957;
  --teal:#5fd1c4;
  --pink:#f7a6c6;
  --blue:#2a8fd6;
}
*{margin:0;padding:0;box-sizing:border-box}
html,body{width:922px;height:1200px;overflow:hidden}
body{font-family:"Arimo",Arial,sans-serif;background:var(--paper)}
.flyer{position:relative;width:922px;height:1200px;overflow:hidden;
  background:linear-gradient(100deg,var(--cream) 0%,#fdf8d6 45%,var(--paper) 80%)}
.headline{position:absolute;left:40px;top:18px;width:680px;font-family:"Roboto Slab",serif;font-weight:800;color:var(--ink);line-height:1.0;letter-spacing:-0.5px}
.headline .line1{font-size:44px}
.headline .accent{color:var(--red);font-size:60px}
.headline .line2{font-size:44px}
.brand{position:absolute;left:705px;top:70px;display:flex;align-items:center;gap:10px}
.brand-dot{width:34px;height:34px;border-radius:50%;background:var(--blue)}
.brand-name{font-family:"Roboto Slab",serif;font-weight:800;font-size:26px;color:var(--blue);line-height:1}
.silhouette{position:absolute;left:38px;top:178px;width:320px;height:320px;
  background:radial-gradient(ellipse at 50% 30%,#3a3a3a 0%,#111 70%);border-radius:150px 150px 0 0}
.case-caption{position:absolute;left:118px;top:458px;font-weight:700;font-size:15px;color:#fff}
.program-title{position:absolute;left:380px;top:212px;width:512px;text-align:right;font-family:"Roboto Slab",serif;font-weight:800;color:var(--ink)}
.program-title .name{font-size:32px;display:block}
.program-title .from{font-size:21px;display:block;margin-top:8px}
.program-title .satisfaction{display:inline-block;background:var(--ink);padding:2px 8px;font-size:23px}
.program-title .satisfaction span:nth-child(1){color:var(--red)}
.program-title .satisfaction span:nth-child(2){color:var(--yellow)}
.program-title .satisfaction span:nth-child(3){color:var(--green)}
.offer{position:absolute;left:378px;top:332px;width:512px;background:var(--violet);border:2px solid #fff;box-shadow:0 0 0 2px var(--violet);padding:6px 16px 8px;font-family:"Roboto Slab",serif;font-weight:700}
.offer-title{color:var(--yellow);font-size:24px}
.offer-title .wow{font-weight:900}
.offer-list{list-style:none;display:grid;grid-template-columns:1fr 1fr;gap:2px 10px;margin:4px 0 4px 28px;color:#fff;font-size:16px}
.offer-list li{display:flex;align-items:center;gap:6px}
.offer-list svg{flex:none}
.offer-contact{color:var(--yellow);font-size:26px}
.panel{position:absolute;left:18px;top:490px;width:890px;height:592px;background:var(--ink);border-radius:34px 34px 40px 40px;color:#fff}
.case-story{position:absolute;left:24px;top:22px;width:440px;font-size:13px;line-height:1.45}
.case-story p{margin-bottom:14px}
.case-story p.tight{margin-bottom:0}
.question{position:absolute;left:24px;top:372px;width:360px;color:var(--teal);font-size:17px;line-height:1.3}
.panel-dot{position:absolute;left:394px;top:368px;width:42px;height:42px;border-radius:50%;background:var(--blue)}
.process{position:absolute;left:478px;top:20px;width:395px;font-size:13px;line-height:1.45}
.process h2{color:var(--green);font-weight:400;font-size:22px;line-height:1.25;margin-bottom:8px}
.process ul{list-style:none;margin-bottom:12px}
.process li{padding-left:12px;position:relative;margin-bottom:4px}
.process li::before{content:"•";position:absolute;left:0}
.process li.alt{color:var(--yellow)}
.process p{margin-bottom:12px}
.process p.values{color:var(--green)}
.bio{position:absolute;left:24px;top:450px;width:850px;color:var(--lime);font-size:17px;line-height:1.3}
.bio strong{font-size:19px}
.contact{position:absolute;left:24px;top:525px;width:850px;text-align:center;color:var(--pink);font-size:18px}
.contact strong{font-size:22px}
</style>
</head>
<body>
<main class="flyer">
  <h1 class="headline">
    <span class="line1">Sometimes the <span class="accent">best financial</span></span><br>
    <span class="accent">advice</span> <span class="line2">isn't about numbers...</span>
  </h1>

  <div class="brand"><span class="brand-dot"></span><span class="brand-name">Harbor Circle</span></div>

  <div class="silhouette" role="img" aria-label="Dark silhouette of a man's head and shoulders representing the client in the case story"></div>
  <p class="case-caption">“Steven” Marlow Heights, PA</p>

  <h2 class="program-title">
    <span class="name">Calm Harbor Blueprint:</span>
    <span class="from">From Financial Worries to <span class="satisfaction"><span>Wealth</span> <span>Satis</span><span>faction</span></span></span>
  </h2>

  <section class="offer">
    <div class="offer-title"><span class="wow">WOW</span> A Six Week Program to</div>
    <ul class="offer-list">
      <li><svg width="14" height="14" viewBox="0 0 14 14"><rect x="0.5" y="0.5" width="13" height="13" fill="#fff"/><path d="M3 7l3 3 5-6" stroke="#000" stroke-width="2" fill="none"/></svg>Reduce stress</li>
      <li><svg width="14" height="14" viewBox="0 0 14 14"><rect x="0.5" y="0.5" width="13" height="13" fill="#fff"/><path d="M3 7l3 3 5-6" stroke="#000" stroke-width="2" fill="none"/></svg>Improve performance</li>
      <li><svg width="14" height="14" viewBox="0 0 14 14"><rect x="0.5" y="0.5" width="13" height="13" fill="#fff"/><path d="M3 7l3 3 5-6" stroke="#000" stroke-width="2" fill="none"/></svg>Restore Control</li>
      <li><svg width="14" height="14" viewBox="0 0 14 14"><rect x="0.5" y="0.5" width="13" height="13" fill="#fff"/><path d="M3 7l3 3 5-6" stroke="#000" stroke-width="2" fill="none"/></svg>Money Back Guarantee</li>
    </ul>
    <div class="offer-contact">Dana Whitfield (215) 555-0148</div>
  </section>

  <section class="panel">
    <div class="case-story">
      <p>A 49 year old attorney, Steve was used to success and rising net worth. But with huge losses in the market crash, layoffs at his firm, his kids heading for college and the stagnant economy stretching ahead, his usual optimism is gone.</p>
      <p class="tight">With his anxiety growing, Steve doubts his own decision making ability. His confidence slipping, he stopped opening his financial statements and could barely speak to his financial advisor. He thought if his advisor said “hang in there” one more time, he just might blow up.</p>
      <p>Yet Steve felt too embarrassed to talk about his deep worries, even with his wife. It seemed like all he could do was pour another glass of wine and suffer in isolation.</p>
      <p>If you're like Steve, you're afraid and alone with plenty of company. In a September 2009 National Wellness Survey Group poll, 80 percent reported the economy is causing significant stress, up from 66 percent from the previous April. The Restful Nights Council said 27 percent of people surveyed had sleeplessness because of economic anxiety.</p>
    </div>
    <p class="question">How can you take control of these worries and get back to enjoying your life?</p>
    <span class="panel-dot"></span>

    <div class="process">
      <h2>In this 5 session coaching process you will:</h2>
      <ul>
        <li>Learn a decision making tool to make choices that truly serve your needs</li>
        <li class="alt">Clarify and more fully engage with your purpose and passions</li>
        <li>Improve your relationship with your financial advisor</li>
        <li class="alt">Feel more in control and confident in your financial life</li>
      </ul>
      <p>This process guides you to step back and understand the source of your financial worry—your unique story about the meaning of money. Your money story drives your emotions and decision making—for better and worse. You'll learn a decision making tool for more conscious, effective and satisfying financial and life decisions.</p>
      <p class="values">You'll also examine your core values and strengths—what really matters most to you and how you work at your best. When you use your money and your core strengths to pursue your highest aspirations, life and wealth become balanced. As you commit more fully to your mission and passions, satisfaction grows and money worries melt away.</p>
    </div>

    <p class="bio"><strong>Dana Whitfield, Ph.D.</strong> is a psychologist with 30 years of experience treating anxiety and stress. She is co-founder and facilitator of Harbor Circle, a peer learning group for high net worth investors.</p>
    <p class="contact">For more information, call <strong>267-555-0193</strong>. &nbsp; dana.whitfield@harborcoach.net</p>
  </section>
</main>
</body>
</html>
```